Need simple and modern looking business card with all my information on one side and logo on the other side
Info :
Company name - VELMAR CONSTRUCTION LLC
Company addres- 418 harbor 87th. Dunmoor park ny 10352
Email- velmarllc@tridomail.Com
Company phone number 555-318-6094
Cell number- 555-742-0583
Web site - velmarllc.Com
My name Gerald tomasino

Target Market(s)

Construction , home improvement, remodeling

Industry/Entity Type

Construction

Contact Information for Business Card

It has to be moder but at the same time simple

Font styles to use
Sans Serif

Colors
0255a3
ffffff
000000
f78f20
b1b1b1
9d9d9d
1b1b1b
33a6d7
ec1f27

Requirements
Must have
• My logo on one side maybe with a some kind of background on the other side all my information
Nice to have
• Some kind of background pictures provided by you .PLEASE HAVE ACCOUNT WITH PIXELVAULT WILL NOT PAY ANY EXTRA FEES .
Should not have
• Any kind of hamer, nails,screws, helmets itp. Please do not copy the other designs come up with something new.

```html
<!DOCTYPE html>
<html lang="en">
<head>
<meta charset="utf-8">
<title>Velmar Construction LLC – Business Card</title>
<link rel="stylesheet" href="https://fonts.googleapis.com/css2?family=Open+Sans:wght@400;600;700&display=swap">
<style>
  :root {
    --stage: #e4e4e4;
    --paper: #ffffff;
    --ink: #1b1b1b;
    --ink-soft: #3d3d3d;
    --orange: #f78f20;
    --red: #ec1f27;
    --blue: #0255a3;
    --grey-light: #b1b1b1;
    --grey-mid: #9d9d9d;
    --slate: #3b3b3d;
    --slate-dark: #262628;
  }
  * { box-sizing: border-box; margin: 0; padding: 0; }
  html, body {
    width: 1200px; height: 900px; overflow: hidden;
    background: var(--stage);
    font-family: "Open Sans", Arial, sans-serif;
  }
  .stage {
    width: 1200px; height: 900px;
    display: flex; flex-direction: column;
    align-items: center; justify-content: center; gap: 40px;
  }
  .card {
    position: relative;
    width: 640px; height: 366px;
    box-shadow: 0 6px 18px rgba(0,0,0,0.18);
    overflow: hidden;
  }

  /* Info side */
  .card--info { background: var(--paper); }
  .info__rule {
    position: absolute; left: 56px; top: 34px; bottom: 34px;
    width: 2px; background: var(--red);
  }
  .info__block { position: absolute; left: 78px; top: 92px; }
  .info__name {
    font-weight: 700; font-size: 19px; color: var(--orange);
    margin-bottom: 14px;
  }
  .info__list { list-style: none; }
  .info__item {
    display: flex; align-items: flex-start; gap: 10px;
    font-size: 15px; line-height: 19px; color: var(--ink-soft);
    margin-bottom: 2px;
  }
  .info__item--address { margin-top: 14px; }
  .info__icon { flex: 0 0 16px; width: 16px; height: 16px; margin-top: 2px; }
  .brand {
    position: absolute; display: flex; align-items: center; gap: 10px;
    font-weight: 700; letter-spacing: 1px;
  }
  .brand__mark { width: 14px; height: 14px; background: var(--orange); }
  .card--info .brand { right: 36px; top: 48px; font-size: 17px; color: var(--ink); }

  /* Logo side */
  .card--logo { background: var(--slate); }
  .logo__band {
    position: absolute; left: 0; right: 0; top: 0; height: 96px;
    background: linear-gradient(180deg, var(--slate-dark) 0%, #2e2e30 100%);
  }
  .card--logo .brand {
    right: 40px; top: 150px; font-size: 24px; color: var(--paper);
  }
</style>
</head>
<body>
<main class="stage">

  <section class="card card--info" aria-label="Business card, contact side">
    <span class="info__rule"></span>
    <div class="info__block">
      <p class="info__name">Gerald tomasino</p>
      <ul class="info__list">
        <li class="info__item">
          <svg class="info__icon" viewBox="0 0 16 16"><circle cx="8" cy="8" r="8" fill="var(--orange)"/><path d="M5.5 4.5h2l.6 2-1 .8a5 5 0 0 0 1.6 1.6l.8-1 2 .6v2c0 .4-.3.6-.7.6A6.3 6.3 0 0 1 4.9 5.2c0-.4.2-.7.6-.7z" fill="#fff"/></svg>
          <span>555-742-0583</span>
        </li>
        <li class="info__item">
          <svg class="info__icon" viewBox="0 0 16 16"><circle cx="8" cy="8" r="8" fill="var(--orange)"/><rect x="5.3" y="3.6" width="5.4" height="8.8" rx="1" fill="#fff"/><rect x="6.2" y="4.8" width="3.6" height="5.6" fill="var(--orange)"/></svg>
          <span>555-318-6094</span>
        </li>
        <li class="info__item">
          <svg class="info__icon" viewBox="0 0 16 16"><circle cx="8" cy="8" r="8" fill="var(--orange)"/><rect x="4" y="5" width="8" height="6" fill="#fff"/><path d="M4 5l4 3.2L12 5" stroke="var(--orange)" stroke-width="1" fill="none"/></svg>
          <span>velmarllc@tridomail.Com</span>
        </li>
        <li class="info__item">
          <svg class="info__icon" viewBox="0 0 16 16"><circle cx="8" cy="8" r="8" fill="var(--orange)"/><circle cx="8" cy="8" r="4" fill="none" stroke="#fff" stroke-width="1"/><path d="M4 8h8M8 4c-1.6 2.4-1.6 5.6 0 8M8 4c1.6 2.4 1.6 5.6 0 8" stroke="#fff" stroke-width="0.9" fill="none"/></svg>
          <span>velmarllc.Com</span>
        </li>
        <li class="info__item info__item--address">
          <svg class="info__icon" viewBox="0 0 16 16"><circle cx="8" cy="8" r="8" fill="var(--orange)"/><path d="M8 3.5a3 3 0 0 1 3 3c0 2.2-3 5.8-3 5.8S5 8.7 5 6.5a3 3 0 0 1 3-3z" fill="#fff"/><circle cx="8" cy="6.5" r="1.1" fill="var(--orange)"/></svg>
          <span>418 harbor 87th.<br>Dunmoor park ny 10352</span>
        </li>
      </ul>
    </div>
    <div class="brand"><span class="brand__mark"></span><span>VELMAR CONSTRUCTION LLC</span></div>
  </section>

  <section class="card card--logo" aria-label="Business card, logo side">
    <div class="logo__band" role="img" aria-label="Faint line drawing of a city skyline across the top band"></div>
    <div class="brand"><span class="brand__mark"></span><span>VELMAR CONSTRUCTION LLC</span></div>
  </section>

</main>
</body>
</html>
```